Anzeigengestaltung für Darstellung der Zentralaussagen einer PR-Agentur
Zielgruppe
Wir suchen ein hochwertiges und anspechendes Design für eine halbseitige (DIN A5) Werbeanzeige, um Insolvenzverwalter auf unsere PR-Arbeit für ihre eignenen Insolvenzfälle aufmerksam zu machen. Idealerweise übernimmt der Insolvenzverwalter also die rechtlichen Aufgaben innerhalb der Insolvenz und wir die kommunikativen, also die Öffentlichkeitsarbeit und interne Kommunikation. Meist schätzen die Anwälte hierbei dann unser breites Netzwerk (zu Journalisten etc.), unser Kommunikationsgefühl und, dass wir zudem rechtliches Verständnis mitbringen.
Unsere Zielgruppe sind somit Anwälte, die im Insolvenzrecht tätig sind, also als Insolvenzverwalter arbeite, sowie Unternehmen, denen eine Insolvenz droht oder sich in einer Insolvenz befinden.
Wir sind eine PR-Agenur, spezialisiert auf das juristische Umfeld. Wir beraten Unternehmen und Anwaltskanzleien, wie sie in Rechtsstreitigkeiten mit der Öffentlihkeit umgehen. Spezialisiert sind wir auf die Insolvenzkommunikation. Hier beraten wir die Insolvenzverwaltung und das von der Insolvenz betroffene Unternehmen in der internen und externen Kommunikation. Hierbei bringen wir als Unternehmen mit unseren Mitarbeitern Fachkenntnisse aus PR, sowie juristische Expertise mit, denn alle unsere Berater haben einen juristischen Abschluss. In einer juristischen Ausnahmesituation wie einer Insolvenz ist es für uns daher leicht, den Sachverhalt zu erfassen. Das hebt uns von anderen PR-Agenturen ab. Wir kümmern uns um alle kommunikativen Fragen, die innerhalb des Unternehmens während der Insolvenz auftreten und um Medienanfragen rund um die Insolvenz von außerhalb (klassische Presseanfragen). Verschwiegenheit und Diskretion gegenüber unserem Mandanten steht für uns dabei stets mit an oberster Stelle.
Aufgabenstellung
Wir möchten die Anzeige möglichst klassisch und seriös halten. Trotzdem sollte sie ins Auge fallen und herausstechen. Visuell sollte sie ansprechend sein und mit symbolhaften Bildern unterstrichen, da wir selbst als Berater nicht in der Anzeige abgebildet sein wollen. Textlich sollte es einen nicht erschlagen. Unsere Hauptdienstleistungen und Zentralaussagen sollten aber drin sein (juristische und kommunikative Expertise, interne und externe Insolvenzkommunikation, kein Ein-Mann-Betrieb, gut vernetzt)

```html
<!DOCTYPE html>
<html lang="de">
<head>
<meta charset="utf-8">
<title>Anzeige Insolvenzkommunikation</title>
<link rel="stylesheet" href="https://fonts.googleapis.com/css2?family=Cinzel:wght@400;500&family=Roboto:wght@300;400&display=swap">
<style>
  :root {
    --page-bg: #ececec;
    --ink-dark: #0a0a0a;
    --ink-white: #ffffff;
    --gold: #b39a2a;
    --text-grey: #3c3c3c;
    --logo-grey: #4a4a48;
  }
  html, body {
    margin: 0;
    width: 1200px;
    height: 1050px;
    overflow: hidden;
    background: var(--page-bg);
  }
  .ad {
    position: absolute;
    left: 40px;
    top: 132px;
    width: 1120px;
    height: 786px;
    background: var(--ink-white);
    overflow: hidden;
  }
  .hero {
    position: absolute;
    left: 0; top: 0;
    width: 1120px;
    height: 462px;
    background:
      radial-gradient(ellipse 420px 140px at 560px 400px, rgba(200,200,200,0.55), rgba(0,0,0,0) 70%),
      radial-gradient(ellipse 520px 260px at 80px 180px, rgba(120,120,120,0.55), rgba(0,0,0,0) 70%),
      linear-gradient(180deg, #111 0%, #1c1c1c 55%, #5a5a5a 82%, #2b2a20 100%);
  }
  .headline {
    position: absolute;
    left: 0; right: 0;
    top: 52px;
    margin: 0;
    text-align: center;
    font-family: "Cinzel", serif;
    font-weight: 400;
    color: var(--ink-white);
    font-size: 50px;
    line-height: 64px;
    letter-spacing: 1px;
  }
  .tagline {
    position: absolute;
    left: 442px;
    top: 216px;
    margin: 0;
    font-family: "Roboto", sans-serif;
    font-weight: 300;
    font-size: 21px;
    line-height: 27px;
    color: var(--gold);
  }
  .band-top {
    position: absolute;
    left: 0; top: 462px;
    width: 1120px; height: 17px;
    background: var(--gold);
  }
  .band-bottom {
    position: absolute;
    left: 0; bottom: 0;
    width: 1120px; height: 10px;
    background: var(--gold);
  }
  .body-copy {
    position: absolute;
    left: 68px;
    top: 530px;
    width: 480px;
    margin: 0;
    font-family: "Roboto", sans-serif;
    font-weight: 300;
    font-size: 16px;
    line-height: 20.7px;
    color: var(--text-grey);
    text-align: justify;
  }
  .brand-name {
    position: absolute;
    left: 600px;
    width: 426px;
    top: 568px;
    margin: 0;
    text-align: center;
    font-family: "Cinzel", serif;
    font-weight: 400;
    font-size: 56px;
    letter-spacing: 2px;
    color: var(--logo-grey);
  }
  .contact {
    position: absolute;
    left: 0; right: 0;
    top: 716px;
    margin: 0;
    text-align: center;
    font-family: "Roboto", sans-serif;
    font-weight: 300;
    font-size: 14px;
    line-height: 20px;
    color: var(--text-grey);
  }
  .contact .sep { color: var(--gold); padding: 0 6px; }
</style>
</head>
<body>
  <article class="ad">
    <div class="hero" role="img" aria-label="Schwarz-weißes Foto: weißer Springer neben umgefallenem schwarzen König auf einem Schachbrett"></div>
    <h1 class="headline">Insolvenzkommunikation<br>braucht den Richtigen O-Ton</h1>
    <p class="tagline">Wir kommunizieren für unsere Mandanten Rechts-<br>und Krisenthemen auf höchstem Niveau</p>
    <div class="band-top"></div>

    <p class="body-copy">Nimust, anturem aborum suntem eosam, omnitia di ulparum quatium et eatem harias de quatur sume velestem il magnis maio dempedi cidellab iur, sin eatiosaerum ere poreptas exceriones eiures delit aut mo venihic tem resequate sunt ut omniet hillendus am, corectio dem ent volliquam a sum rem nis cuptureperum idus eum velenduntio veniminti reptatem verferspe.</p>

    <p class="brand-name">MERIDIAN</p>

    <p class="contact">
      MERIDIAN Rechtskommunikation GmbH<span class="sep">|</span>Lindenallee 14<span class="sep">|</span>10115 Berlin<span class="sep">|</span>Tel.: +49 30 12 34 5670<span class="sep">|</span>Fax: +49 30 12 34 5671<br>
      kontakt@meridian-pr.example<span class="sep">|</span>meridian-rechtskommunikation.example
    </p>
    <div class="band-bottom"></div>
  </article>
</body>
</html>
```